Banner ads for VL that work with same theme as below banners

Love the banner ads below. Need more with attached photos. But use the same wording, font as in below banner ads. Should be VL size 1200/627 so I can use for Trovique and VL. Looking for great ads to use as VL ads. We do lots of ads so it will be worth your time to enter this contest you will be rewarded with a ton of work. Need several banner ads that work together. So maybe 1 of the dresses, 1 of the sweater, 1 of the leggings, 1 of the jacket

Target Market(s)

Women 24-45

Industry/Entity Type

Fashion

Requirements
Must have
• Banner ads that work for VL and Trovique
Nice to have
• Several options to choose from
Should not have
• not sure

```html
<!DOCTYPE html>
<html lang="en">
<head>
<meta charset="utf-8">
<title>Our Best Sweater Ever – Shop the Look</title>
<link rel="stylesheet" href="https://fonts.googleapis.com/css2?family=Playball&family=Roboto+Slab:wght@400;700&display=swap">
<style>
  :root {
    --ink: #585d8c;
    --paper: #ffffff;
    --fog-light: #f1f1f2;
    --fog-mid: #d6d6d8;
    --fog-dark: #b9b9bc;
    --lilac: #c9c7db;
    --veil: rgba(150, 152, 190, 0.28);
  }
  html, body {
    margin: 0;
    padding: 0;
    overflow: hidden;
    background: #ffffff;
  }
  .banner {
    position: relative;
    width: 1200px;
    height: 627px;
    overflow: hidden;
    font-family: "Roboto Slab", Georgia, serif;
  }
  .backdrop-scene {
    position: absolute;
    inset: 0;
    background:
      radial-gradient(ellipse at 30% 20%, var(--fog-light) 0%, transparent 60%),
      linear-gradient(90deg, var(--fog-dark) 0%, var(--fog-mid) 22%, var(--fog-light) 45%, var(--fog-mid) 75%, var(--fog-dark) 100%);
  }
  .model-photo {
    position: absolute;
    left: 240px;
    top: 0;
    width: 360px;
    height: 627px;
    background:
      linear-gradient(180deg, transparent 0%, transparent 24%, var(--lilac) 30%, var(--lilac) 92%, transparent 96%) 50px 0 / 240px 100% no-repeat,
      linear-gradient(90deg, #f4f4f6 0%, #ffffff 40%, #f0f0f2 100%);
    clip-path: polygon(0 0, 100% 0, 88% 100%, 0 100%);
  }
  .veil {
    position: absolute;
    inset: 0;
    width: 1200px;
    height: 627px;
  }
  .offer-frame {
    position: absolute;
    left: 718px;
    top: 150px;
    width: 334px;
    height: 328px;
    box-sizing: border-box;
    border: 2px solid var(--ink);
    border-bottom: none;
  }
  .offer-box {
    position: absolute;
    left: 75px;
    top: 78px;
    width: 189px;
    height: 177px;
    box-sizing: border-box;
    border: 3px solid var(--ink);
    display: flex;
    flex-direction: column;
    align-items: center;
    justify-content: space-between;
    color: var(--ink);
  }
  .offer-script {
    font-family: "Playball", cursive;
    font-size: 34px;
    line-height: 1;
    margin: 0;
  }
  .offer-script.top { padding-top: 18px; }
  .offer-script.bottom { padding-bottom: 14px; }
  .offer-product {
    width: 100%;
    background: var(--ink);
    color: var(--paper);
    font-weight: 700;
    font-size: 27px;
    letter-spacing: 2px;
    text-align: center;
    line-height: 40px;
    margin: 0;
  }
  .cta {
    position: absolute;
    left: -2px;
    right: -2px;
    bottom: -10px;
    display: flex;
    align-items: center;
    gap: 10px;
    color: var(--ink);
    font-size: 17px;
    letter-spacing: 1.5px;
    text-decoration: none;
    white-space: nowrap;
  }
  .cta::before, .cta::after {
    content: "";
    flex: 1;
    height: 2px;
    background: var(--ink);
  }
  .cta strong { font-weight: 700; }
</style>
</head>
<body>
  <main class="banner">
    <div class="backdrop-scene" role="img" aria-label="Misty winter forest with bare trees in soft grey fog"></div>
    <div class="model-photo" role="img" aria-label="Woman with long wavy hair wearing an oversized lilac turtleneck sweater and black leggings"></div>
    <svg class="veil" viewBox="0 0 1200 627" aria-hidden="true">
      <polygon points="560,365 720,148 1052,148 1052,480 960,627 800,627" fill="var(--veil)"/>
    </svg>
    <section class="offer-frame">
      <div class="offer-box">
        <p class="offer-script top">Our Best</p>
        <h1 class="offer-product">SWEATER</h1>
        <p class="offer-script bottom">Ever !</p>
      </div>
      <a class="cta" href="#"><span><strong>SHOP</strong> THE <strong>LOOK</strong></span></a>
    </section>
  </main>
</body>
</html>
```